Lumvex Crating Business Card

Project Overview
We are seeking a modern, minimalist business card that effectively represents our company while making a bold and lasting impression. The design should reflect trust, professionalism, and innovation, reinforcing our expertise in custom plastic manufacturing for warehouse and distribution centers.

Provided Assets & Specifications
Logo: We will provide our official logo for integration into the design.
Design Files: Photoshop (PSD) files for our printing specifications will be supplied.

Card Size & Material:
Dimensions: 3.5" x 2"
Material: 1/8" Radius Plastic Business Cards with 1/8" Rounded Corners
Clear plastic background—the design should strategically incorporate transparency.
Orientation: The card should be designed in landscape format for a sleek and professional presentation.

Design Requirements:
Logo Prominence
The logo must be the focal point of the card.
Space should be used effectively to draw attention to the logo while maintaining a minimalist layout.

Clear Plastic Integration
The transparent background should create the illusion of blank space, enhancing the modern and high-quality feel.
Avoid any frosted effects—we do not want white areas to appear semi-transparent.

Minimalist & Impactful
Clean, structured, and easy to read at a glance.
Focus on sharp contrast to ensure legibility and visibility.
The design should instill confidence and reflect our role as a leading plastics manufacturer.

Color Palette & Contrast
Primary Colors: Blue, Black, White, and Grey
Use bold black or blue for text and key elements to ensure they stand out against the clear plastic.
Avoid light, pastel, or neon colors that may fade into the plastic background.
No frosted or semi-transparent white—we do not want a cloudy effect.

Typography & Information Hierarchy
Bold, modern typography—clear, professional, and highly legible.
The business card should highlight:
Company Logo (Primary Focus)
Full Name & Title
Phone Number
Email
Website

Brand Representation
The card should reflect our expertise in manufacturing high-quality custom plastics for large-scale packaging and distribution businesses.
Our clients rely on us to enhance their brand presence through custom plastic solutions, and our business cards should reinforce that sense of precision and trust.

Final Considerations
Utilize the clear plastic effectively to differentiate our brand from standard business cards.
Maintain a sleek, professional aesthetic while ensuring all text and elements remain legible.
The design should align with our industry, conveying reliability and innovation.
We look forward to seeing a design that captures our brand identity, maximizes the clear plastic medium, and makes a strong, professional impact on our clients.

```html
<!DOCTYPE html>
<html lang="en">
<head>
<meta charset="utf-8">
<title>Lumvex Crating Business Card</title>
<link href="https://fonts.googleapis.com/css2?family=Lato:wght@400;700&display=swap" rel="stylesheet">
<style>
  :root {
    --stage: #3c3c3e;
    --card-dark: #2f2f31;
    --card-light: #ffffff;
    --ink: #2b2b2d;
    --blue: #0a86c4;
    --white: #ffffff;
  }
  * { box-sizing: border-box; margin: 0; padding: 0; }
  html, body {
    width: 1200px; height: 689px; overflow: hidden;
    background: var(--stage);
    font-family: "Lato", Arial, sans-serif;
  }
  .stage {
    width: 1200px; height: 689px;
    display: flex; align-items: center; justify-content: center; gap: 50px;
  }
  .card {
    position: relative;
    width: 525px; height: 300px;
    border-radius: 18px;
    overflow: hidden;
  }
  .card-front { background: var(--card-dark); }
  .card-back { background: var(--card-light); color: var(--ink); }

  .brand {
    display: flex; align-items: center; gap: 14px;
    font-weight: 700; letter-spacing: 0.02em;
  }
  .brand-square { display: block; background: var(--blue); }
  .card-front .brand {
    position: absolute; inset: 0; justify-content: center;
    color: var(--white); font-size: 44px;
  }
  .card-front .brand-square { width: 40px; height: 40px; }

  .card-back .brand {
    position: absolute; top: 52px; right: 34px;
    color: var(--ink); font-size: 27px; gap: 10px;
  }
  .card-back .brand-square { width: 26px; height: 26px; }

  .person { position: absolute; left: 36px; top: 118px; }
  .person-name { font-size: 25px; font-weight: 400; letter-spacing: 0.01em; text-transform: uppercase; }
  .person-title { font-size: 16px; margin-top: 4px; }

  .divider {
    position: absolute; left: 36px; right: 34px; top: 186px;
    height: 1px; background: var(--ink);
  }

  .contact { position: absolute; left: 36px; top: 198px; list-style: none; font-size: 15px; }
  .contact li { display: flex; align-items: center; gap: 10px; line-height: 24px; }
  .contact svg { width: 15px; height: 15px; fill: var(--blue); flex: none; }

  .address {
    position: absolute; right: 34px; top: 196px;
    text-align: right; font-size: 14px; line-height: 20px;
  }

  .footer-band { position: absolute; left: 0; bottom: 0; width: 525px; height: 56px; }
  .website {
    position: absolute; right: 30px; bottom: 12px;
    color: var(--white); font-size: 14px; letter-spacing: 0.02em;
  }
</style>
</head>
<body>
<main class="stage">
  <section class="card card-front" aria-label="Card front">
    <div class="brand"><span class="brand-square"></span>Lumvex Crating</div>
  </section>

  <section class="card card-back" aria-label="Card back">
    <div class="brand"><span class="brand-square"></span>Lumvex Crating</div>

    <div class="person">
      <h1 class="person-name">Marcus Delaney</h1>
      <p class="person-title">Owner</p>
    </div>

    <div class="divider"></div>

    <ul class="contact">
      <li>
        <svg viewBox="0 0 24 24" aria-hidden="true"><path d="M6.6 10.8a15.1 15.1 0 0 0 6.6 6.6l2.2-2.2a1 1 0 0 1 1-.25 11.4 11.4 0 0 0 3.6.57 1 1 0 0 1 1 1V20a1 1 0 0 1-1 1A17 17 0 0 1 3 4a1 1 0 0 1 1-1h3.5a1 1 0 0 1 1 1c0 1.25.2 2.45.57 3.57a1 1 0 0 1-.25 1z"/></svg>
        052-418 730 264
      </li>
      <li>
        <svg viewBox="0 0 24 24" aria-hidden="true"><path d="M2 5h20v14H2z M2 5l10 8 10-8" /></svg>
        hello@lumvexcrating.com
      </li>
    </ul>

    <p class="address">87 Harbor Yard Road, Dock 4<br>30218, Portland</p>

    <svg class="footer-band" viewBox="0 0 525 56" aria-hidden="true">
      <polygon points="0,42 330,42 326,50 0,50" fill="var(--blue)"/>
      <polygon points="326,56 346,16 525,16 525,56" fill="var(--card-dark)"/>
    </svg>
    <span class="website">www.lumvexcrating.com</span>
  </section>
</main>
</body>
</html>
```